Thornwell Building Company - advertisement poster

I am looking to print some canvas signs to advertise my general contracting company, Thornwell Building Company. The sign will measure 6' long x 3' high so the size should match that ratio. I already have a logo icon, which is the Letter 'A' and some trees that I would like to incorporate, see attached. I would also like the to have the following information listed:
1) phone number: 472-318-6095
2) email: thornwellbuildingcompany@mailvistra.net
3) website: thornwellbuildingcompany.com
4) Lic#5386204
5) I want to use this text: "BUILD WITH THE T-CREW!"

The ad should be relatively simple and clean. Black and Green are my company colors. I am open to creative ideas!

Target Market(s)

People looking to renovate their homes

Industry/Entity Type

Construction

Colors
59FF00
82FF00
B8FF75
E3FFCB
F4FFEA

Requirements
Must have
• Must have my company logo
Should not have
• No photos or complex graphics

```html
<!DOCTYPE html>
<html lang="en">
<head>
<meta charset="utf-8">
<title>Thornwell Building Company – Sign</title>
<link rel="stylesheet" href="https://fonts.googleapis.com/css2?family=League+Gothic&family=Michroma&display=swap">
<style>
  :root {
    --surround: #2d2e46;
    --navy: #35346a;
    --green: #75b54f;
    --white: #ffffff;
  }
  * { margin: 0; padding: 0; box-sizing: border-box; }
  html, body {
    width: 1200px; height: 722px; overflow: hidden;
    background: var(--surround);
  }
  .sign {
    position: absolute; left: 129.5px; top: 125.5px;
    width: 940.5px; height: 470.5px;
    background: var(--white);
    font-family: "League Gothic", "Oswald", sans-serif;
  }
  .contact-panel {
    position: absolute; left: 502px; top: 0; right: 0; bottom: 0;
    background: var(--green);
  }
  .contact-panel .stripe {
    position: absolute; left: 0; right: 0; top: 398.5px; height: 7px;
    background: var(--white);
  }
  .accent-bar {
    position: absolute; left: 0; top: 83.5px; width: 169px; height: 8px;
    background: var(--navy);
  }
  .brand {
    position: absolute; left: 0; width: 502px; text-align: center;
    color: var(--navy);
  }
  .brand-est {
    top: 168px; font-family: "Michroma", sans-serif; font-size: 13px;
    letter-spacing: 6px; display: flex; justify-content: space-between;
    padding: 0 40px 0 48px;
  }
  .brand-name {
    top: 200px; font-family: "League Gothic", sans-serif;
    font-size: 64px; line-height: 1; letter-spacing: 3px; text-transform: uppercase;
  }
  .brand-name span { display: block; font-size: 34px; letter-spacing: 6px; margin-top: 6px; }
  .brand-phone {
    top: 310px; font-family: "Michroma", sans-serif; font-size: 18px; letter-spacing: 5px;
  }
  .brand-tagline {
    top: 387px; font-family: "Michroma", sans-serif; font-size: 19px; letter-spacing: 5px;
  }
  .headline {
    position: absolute; top: 53px; left: 359px; white-space: nowrap;
    font-size: 72px; line-height: 1; letter-spacing: 0.5px;
  }
  .headline .lead { color: var(--navy); }
  .headline .rest { color: var(--white); margin-left: 12px; }
  .contact-row {
    position: absolute; left: 524px; display: flex; align-items: center;
    color: var(--white); white-space: nowrap;
  }
  .contact-row .icon {
    width: 39px; height: 39px; flex: none; margin-right: 18px;
  }
  .row-phone { top: 136px; font-size: 78px; line-height: 1; letter-spacing: 1px; }
  .row-email { top: 210px; font-size: 25px; }
  .row-web { top: 264px; font-size: 31px; }
  .license {
    position: absolute; left: 578px; top: 316px;
    color: var(--white); font-size: 80px; line-height: 1; letter-spacing: 1px;
  }
</style>
</head>
<body>
  <main class="sign">
    <div class="contact-panel"><div class="stripe"></div></div>
    <div class="accent-bar"></div>

    <div class="brand brand-est"><span>ESTD</span><span>2020</span></div>
    <div class="brand brand-name">Thornwell<span>Building Company</span></div>
    <div class="brand brand-phone">472.318.6095</div>
    <div class="brand brand-tagline">JOIN THE T-CREW!</div>

    <h1 class="headline" style="font-weight:400"><span class="lead">BUILD</span><span class="rest">WITH THE T-CREW!</span></h1>

    <div class="contact-row row-phone">
      <svg class="icon" viewBox="0 0 40 40" aria-hidden="true">
        <circle cx="20" cy="20" r="19" fill="var(--white)"/>
        <path d="M13 11c1-1 2.5-1 3 0l2 4c.4 1 0 1.8-.8 2.4l-1 .8c1 2.6 3 4.6 5.6 5.6l.8-1c.6-.8 1.4-1.2 2.4-.8l4 2c1 .5 1 2 0 3l-1.6 1.6c-1.4 1.4-4 1-7-1-3-2-5.6-4.6-7.6-7.6-2-3-2.4-5.6-1-7z" fill="none" stroke="var(--green)" stroke-width="2.2"/>
      </svg>
      <span>472-318-6095</span>
    </div>
    <div class="contact-row row-email">
      <svg class="icon" viewBox="0 0 40 40" aria-hidden="true">
        <circle cx="20" cy="20" r="19" fill="var(--white)"/>
        <rect x="9" y="13" width="22" height="14" fill="none" stroke="var(--green)" stroke-width="2"/>
        <path d="M9 13l11 8 11-8M9 27l8-7M31 27l-8-7" fill="none" stroke="var(--green)" stroke-width="2"/>
      </svg>
      <span>thornwellbuildingcompany@mailvistra.net</span>
    </div>
    <div class="contact-row row-web">
      <svg class="icon" viewBox="0 0 40 40" aria-hidden="true">
        <circle cx="20" cy="20" r="19" fill="var(--white)"/>
        <g fill="none" stroke="var(--green)" stroke-width="2">
          <circle cx="20" cy="20" r="10"/>
          <ellipse cx="20" cy="20" rx="4.5" ry="10"/>
          <path d="M10 20h20M12 15h16M12 25h16M20 10v20"/>
        </g>
      </svg>
      <span>thornwellbuildingcompany.com</span>
    </div>

    <div class="license">Lic#5386204</div>
  </main>
</body>
</html>
```